International Company needs a Letterhead & Envelope Design

Our Company name is Corvale Brightwick Limited.
We'd like to ask the Designers for the luxurious and sophisticated design. Our logo is very simple and neat with letter logos, so we look forward to more professional and refined designs from Designers.
We look forward to providing you with a great design.
Thanks very much in advance.

```html
<!DOCTYPE html>
<html lang="en">
<head>
<meta charset="utf-8">
<title>Corvale Brightwick Limited — Stationery</title>
<link rel="stylesheet" href="https://fonts.googleapis.com/css2?family=Open+Sans:wght@400;700&display=swap">
<style>
  :root {
    --backdrop: #707070;
    --paper: #eeeeee;
    --ink: #58585a;
    --ink-soft: #5e5e60;
    --rule: #9a9a9a;
    --white: #ffffff;
    --shadow: 0 2px 7px rgba(0, 0, 0, 0.38), 0 0 1px rgba(0, 0, 0, 0.45);
  }
  * { margin: 0; padding: 0; box-sizing: border-box; }
  html, body { width: 1200px; height: 947px; overflow: hidden; }
  body {
    background: var(--backdrop);
    font-family: "Open Sans", Arial, sans-serif;
    position: relative;
  }
  .wordmark {
    font-family: "Open Sans", Arial, sans-serif;
    font-weight: 700;
    color: var(--ink);
    letter-spacing: 0.5px;
    line-height: 1;
    position: absolute;
    white-space: nowrap;
  }

  /* Letterhead */
  .letterhead {
    position: absolute;
    left: 57px; top: 82px;
    width: 557px; height: 781px;
    background: var(--paper);
    box-shadow: var(--shadow);
  }
  .letterhead__edge {
    position: absolute; left: 0; top: 0;
    width: 13px; height: 100%;
    background: var(--ink);
  }
  .letterhead .wordmark { left: 47px; top: 81px; font-size: 22px; }
  .letterhead__contact {
    position: absolute;
    left: 421px; top: 52px;
    padding-left: 11px;
    border-left: 1px solid var(--rule);
    font-size: 7.4px;
    color: var(--ink-soft);
    line-height: 9.6px;
  }
  .letterhead__address { margin-bottom: 5px; }
  .contact-line { display: flex; align-items: center; height: 11px; }
  .contact-line svg { width: 7px; height: 7px; margin-right: 6px; fill: var(--ink); flex: none; }

  /* Envelope back with flap */
  .envelope-back {
    position: absolute;
    left: 570px; top: 381px;
    width: 579px; height: 289px;
    background: var(--paper);
    box-shadow: var(--shadow);
  }
  .envelope-back__flap { position: absolute; left: 0; top: 0; width: 579px; height: 83px; }
  .envelope-back .wordmark {
    color: var(--white);
    font-size: 20px;
    left: 0; right: 0; top: 33px;
    text-align: center;
  }

  /* Envelope front */
  .envelope-front {
    position: absolute;
    left: 475px; top: 532px;
    width: 634px; height: 289px;
    background: var(--paper);
    box-shadow: var(--shadow);
  }
  .envelope-front__edge {
    position: absolute; left: 0; top: 0;
    width: 10px; height: 100%;
    background: var(--ink);
  }
  .envelope-front__sender {
    position: absolute;
    left: 40px; top: 29px;
    width: 96px;
    text-align: center;
  }
  .envelope-front .wordmark { position: static; font-size: 18px; display: block; }
  .envelope-front__address {
    margin-top: 6px;
    font-size: 7.4px;
    line-height: 9.6px;
    color: var(--ink-soft);
  }
</style>
</head>
<body>

<section class="letterhead" aria-label="Letterhead">
  <div class="letterhead__edge"></div>
  <div class="wordmark">CORVALE</div>
  <div class="letterhead__contact">
    <div class="letterhead__address">2716 Ashgrove Lane<br>Millbrook, NY 12545</div>
    <div class="contact-line">
      <svg viewBox="0 0 10 10" aria-hidden="true"><path d="M1 3 Q5 0 9 3 V4 H7 V3 H3 V4 H1 Z M2 5 H8 L9 9 H1 Z"/></svg>
      555 0142 7781
    </div>
    <div class="contact-line">
      <svg viewBox="0 0 10 10" aria-hidden="true"><path d="M3 0 H7 Q8 0 8 1 V9 Q8 10 7 10 H3 Q2 10 2 9 V1 Q2 0 3 0 Z M3 1.5 V7.5 H7 V1.5 Z"/></svg>
      555 0196 3304
    </div>
    <div class="contact-line">
      <svg viewBox="0 0 10 10" aria-hidden="true"><path d="M3 0 H7 V3 H3 Z M0 4 H10 V8 H8 V10 H2 V8 H0 Z M3 7 V9 H7 V7 Z"/></svg>
      555 0158 2269
    </div>
    <div class="contact-line">
      <svg viewBox="0 0 10 10" aria-hidden="true"><path d="M0 2 H10 V3 L5 6 L0 3 Z M0 4.2 L5 7.2 L10 4.2 V8 H0 Z"/></svg>
      elena@corvale.com
    </div>
    <div class="contact-line">
      <svg viewBox="0 0 10 10" aria-hidden="true"><circle cx="5" cy="5" r="4.5"/></svg>
      www.corvale.com
    </div>
  </div>
</section>

<section class="envelope-back" aria-label="Envelope, back">
  <svg class="envelope-back__flap" viewBox="0 0 579 83" aria-hidden="true">
    <path d="M0 0 H579 L566 60 Q561 83 538 83 H41 Q18 83 13 60 Z" fill="var(--ink)"/>
  </svg>
  <div class="wordmark">CORVALE</div>
</section>

<section class="envelope-front" aria-label="Envelope, front">
  <div class="envelope-front__edge"></div>
  <div class="envelope-front__sender">
    <span class="wordmark">CORVALE</span>
    <div class="envelope-front__address">2716 Ashgrove Lane<br>Millbrook, NY 12545</div>
  </div>
</section>

</body>
</html>
```